Business Card Design Project and Logo Enhancement

This project requires designing a business card for a construction company. It also requires small enhancements on provided logo.
Summary about the company:
Name: Korvellan Group.
Future website. www.korvellan.ca
Korvellan is a home redesign and renovation company providing services in Ottawa Canada area.
It offers the following services:
- Home Additions
- Roofing
- Eavestroughing & Soffit Fascia
- Fencing
- Decks
- Window Installation, and
- Indoor Renovation Including ( Kitchen redesign, Basement finishing, bathroom upgrades, etc)
Logo and Company name background:
Korvellan refers to an ancient empire that was located in Balkans called Veltarians.
Provided logo represents the symbol of Veltarians.
Project Expectation:
Logo:
Attached logo is too SIMPLe. It would be nice adding a bit of design.
That could include different colors or adding a bit of style to the logo.
Business Card
Initial preferred layout/content ( open to other suggestions) :
Preferred type: Vertical with rounded corners
Front side should have:
- Logo
- Company Name
- First Name/ Last name: Ie: Edmir Kollqaj
- Office Phone:
- Direct Phone:
- QR Code linking to www.korvellan.ca, and
- website url. www. korvellan.ca
Back end shall contain:
Professional services offered:
- Large company logo covering most of the card as a water mark
- Divisions Services offered
- Roofing
- Eavestroughing, Soffit, Fascia
- Fencing and Decks
- Indoor Design and Renovation
- Company Phone and
- Company website address: www.korvellan.ca
PSD and other raw files must be provided by the winner.

```html
<!DOCTYPE html>
<html lang="en">
<head>
<meta charset="UTF-8">
<title>Korvellan Group – Business Card</title>
<link rel="stylesheet" href="https://fonts.googleapis.com/css2?family=Tinos:ital,wght@0,400;1,400&display=swap">
<style>
  :root {
    --page-bg: #ffffff;
    --gold-edge: #b08a5f;
    --gold-mid: #d8bf97;
    --gold-light: #fcf2de;
    --gold-glow: #fef6e6;
    --brand-red: #6e2518;
    --heading-brown: #3b1c13;
    --tagline-grey: #3d3a36;
    --label-brown: #5b2a1d;
    --value-red: #b22a22;
    --body-ink: #141210;
    --shadow: rgba(60, 45, 30, 0.45);
  }
  * { margin: 0; padding: 0; box-sizing: border-box; }
  html, body {
    width: 707px;
    height: 1200px;
    overflow: hidden;
    background: var(--page-bg);
  }
  .canvas {
    position: relative;
    width: 707px;
    height: 1200px;
    font-family: "Tinos", "Times New Roman", serif;
  }
  .card {
    position: absolute;
    left: 8px;
    top: 8px;
    width: 682px;
    height: 1176px;
    border-radius: 38px;
    background: linear-gradient(90deg,
      var(--gold-edge) 0%,
      var(--gold-mid) 22%,
      var(--gold-light) 48%,
      var(--gold-glow) 57%,
      var(--gold-mid) 80%,
      var(--gold-edge) 100%);
    box-shadow: 4px 6px 8px var(--shadow);
    overflow: hidden;
  }
  .watermark-area {
    position: absolute;
    left: 100px;
    top: 255px;
    width: 500px;
    height: 620px;
    border-radius: 50%;
    background: radial-gradient(ellipse at center, rgba(176,138,95,0.12) 0%, rgba(176,138,95,0) 70%);
  }
  .centered {
    position: absolute;
    left: 0;
    width: 718px;
    text-align: center;
    line-height: 1;
    white-space: nowrap;
  }
  .company-name {
    top: 172px;
    font-size: 75px;
    color: var(--brand-red);
  }
  .tagline {
    top: 268px;
    font-size: 34px;
    color: var(--tagline-grey);
  }
  .services-heading {
    top: 453px;
    font-size: 37px;
    color: var(--heading-brown);
  }
  .services-list {
    position: absolute;
    left: 89px;
    top: 575px;
    list-style: none;
    font-style: italic;
    font-size: 24px;
    line-height: 34px;
    color: var(--body-ink);
  }
  .contact {
    position: absolute;
    left: 0;
    top: 858px;
    width: 704px;
    text-align: center;
    font-size: 33px;
    line-height: 43.5px;
    color: var(--label-brown);
  }
  .contact .value { color: var(--value-red); }
  .service-area {
    top: 1083px;
    font-size: 21px;
    color: var(--body-ink);
  }
</style>
</head>
<body>
  <div class="canvas">
    <div class="card"></div>
    <div class="watermark-area" role="img" aria-label="Faint company emblem watermark behind the services list"></div>

    <h1 class="centered company-name" style="font-weight:400">Korvellan Group</h1>
    <p class="centered tagline">Home Redesign &amp; Renovation</p>

    <h2 class="centered services-heading" style="font-weight:400">Professional services offered:</h2>
    <ul class="services-list">
      <li>- Home Additions</li>
      <li>- Roofing</li>
      <li>- Eavestroughing, Soffit, Fascia</li>
      <li>- Fencing and Decks</li>
      <li>- Window Installation</li>
      <li>- Indoor Design and Renovation</li>
    </ul>

    <div class="contact">
      <p>Office: <span class="value">613.555.0142</span></p>
      <p>Direct: <span class="value">613.555.018</span></p>
      <p>Web: <span class="value">www.korvellan.ca</span></p>
    </div>

    <p class="centered service-area">Providing Services in Ottawa Canada Area</p>
  </div>
</body>
</html>
```